Business Card Design Project

The logo I included in my order was a previous image that we've used for shirts, signs, magnets, etc. We've decided to go back to that logo, with some updates.
We need to add "Inc." after "Brindell Roofing,"
Also, I need the logo with a transparent background so that I can use it on other projects.

The business cards will be the first item I order with the new logo. The employee's info is:
Derek Palp
Sales Manager
610-743-2956
dpalp@brindellroofinginc.example

Also, I want a "Find us on Chatterbook" icon on the card, along with our web address, www.brindellroofinginc.example.

Any questions, please email or call me:
norabrindell@mailvex.example
610-918-6032

Project Deadline Extended
Reason: This is the first time I've tried Pixel Guild.

My timetable changed and I need to select a design by the end of the work day, 6 hours from now.Thanks so much for all of the super designs.

Target Market(s)

Homeowners

Industry/Entity Type

Business

Font styles to use
Serif

Requirements
Must have
• Transparent background
Similar to logo in photo I sent you

```html
<!DOCTYPE html>
<html lang="en">
<head>
<meta charset="utf-8">
<title>Brindell Roofing Inc. – Business Card</title>
<link rel="stylesheet" href="https://fonts.googleapis.com/css2?family=Cinzel:wght@400;700&family=PT+Sans+Narrow:wght@400;700&display=swap">
<style>
  :root {
    --backdrop: #2b211c;
    --card-dark: #1f1f1f;
    --card-glow: #3a3a3a;
    --brand-lime: #d9da8c;
    --band-lime: #b8b94b;
    --band-edge: #dcdc95;
    --text-light: #ececec;
    --text-dark: #2b2b1f;
  }
  html, body {
    margin: 0;
    padding: 0;
    width: 1200px;
    height: 1000px;
    overflow: hidden;
    background: var(--backdrop);
  }
  .business-card {
    position: absolute;
    left: 353px;
    top: 64px;
    width: 494px;
    height: 864px;
    background: radial-gradient(ellipse 70% 45% at 50% 28%, var(--card-glow), var(--card-dark) 75%);
    font-family: "Cinzel", serif;
    color: var(--text-light);
    overflow: hidden;
  }
  .brand-name {
    position: absolute;
    top: 238px;
    left: 0;
    width: 100%;
    text-align: center;
    color: var(--brand-lime);
    font-family: "Cinzel", serif;
    font-weight: 700;
    font-size: 46px;
    line-height: 56px;
  }
  .employee-name {
    position: absolute;
    top: 384px;
    width: 100%;
    text-align: center;
    font-size: 46px;
    letter-spacing: 1px;
    text-shadow: 0 2px 3px #000;
  }
  .employee-title {
    position: absolute;
    top: 452px;
    width: 100%;
    text-align: center;
    font-family: "PT Sans Narrow", sans-serif;
    font-size: 22px;
    text-transform: uppercase;
  }
  .employee-phone {
    position: absolute;
    top: 475px;
    width: 100%;
    text-align: center;
    font-size: 34px;
  }
  .employee-email {
    position: absolute;
    top: 522px;
    width: 100%;
    text-align: center;
    font-size: 18px;
  }
  .contact-band {
    position: absolute;
    left: 0;
    bottom: 0;
    width: 100%;
    height: 158px;
    background: var(--band-lime);
    border-top: 3px solid var(--band-edge);
    color: var(--text-dark);
  }
  .social-link {
    position: absolute;
    left: 20px;
    bottom: 26px;
    font-family: "PT Sans Narrow", sans-serif;
    font-weight: 700;
    color: var(--text-dark);
    line-height: 1;
  }
  .social-link .lead { font-size: 15px; display: block; }
  .social-link .network { font-size: 22px; display: block; margin-top: 2px; }
  .company-phone {
    position: absolute;
    right: 20px;
    top: 54px;
    font-size: 34px;
  }
  .company-web {
    position: absolute;
    right: 20px;
    top: 104px;
    font-size: 22px;
  }
  .company-web small { font-size: 14px; }
</style>
</head>
<body>
  <main class="business-card">
    <div class="brand-name">Brindell<br>Roofing Inc.</div>

    <div class="employee-name">Derek Palp</div>
    <div class="employee-title">Sales Manager</div>
    <div class="employee-phone">(610) 743-2956</div>
    <div class="employee-email">dpalp@BrindellRoofingInc.example</div>

    <section class="contact-band">
      <div class="social-link">
        <span class="lead">Find us on:</span>
        <span class="network">Chatterbook</span>
      </div>
      <div class="company-phone">(610) 555-0174</div>
      <div class="company-web">BrindellRoofingInc<small>.example</small></div>
    </section>
  </main>
</body>
</html>
```